Web Design for ORV Air conditioning company

Hello,

I am calling on you for the modernization of the company's website
https://clim-solaris-atelier.fr/

The new one must include the new logo with the new graphic charter (color, style ...)

I'm looking for a simple design (less is more), a font written without Serif, the logo that brings a touch of color and modernity.

(maintenance and installation company for air conditioning and ventilation systems)
COLORS: in line with the logo

CHAPTER:

# PRESENTATION
# SERVICES
AIR CONDITIONING (ice cube icon)
HEATING (flame icon)
AIR TREATMENT (icon fan)
# ACHIEVEMENTS

# CONTACT
CONTACT FORM
GOOGLE MAPS

Target Market(s)

Showcase site for our customers

Coding

Coded - Design and coding required

Number of Pages Required

4 page

Font styles to use
Sans Serif

Colors
33b8a4
33a6d7
3176b5
ffffff

Requirements
Must have
• Clear and fluid navigation
a visual identity of the page with the logo
Should not have
• Overloaded.

```html
<!DOCTYPE html>
<html lang="en">
<head>
<meta charset="utf-8">
<title>ORV – Solaris Climate Atelier</title>
<link href="https://fonts.googleapis.com/css2?family=Roboto:wght@400;500;700&family=Questrial&display=swap" rel="stylesheet">
<style>
:root{
  --green:#3db48a;
  --teal:#3aa0ad;
  --blue:#3495b8;
  --ink:#262b30;
  --body:#6b7278;
  --line:#d8dde0;
  --footer:#202225;
  --white:#ffffff;
  --grad:linear-gradient(90deg,#52b48a 0%,#3a9fae 55%,#3495b8 100%);
}
*{margin:0;padding:0;box-sizing:border-box}
html,body{width:1200px;height:2958px;overflow:hidden}
body{font-family:"Questrial",sans-serif;color:var(--ink);background:var(--white);position:relative}
.head,.h{font-family:"Roboto",sans-serif}
.abs{position:absolute}

/* header */
.topbar{position:absolute;left:0;top:0;width:1200px;height:73px}
.brand{position:absolute;left:93px;top:8px;text-align:center}
.brand-name{font-family:"Roboto",sans-serif;font-weight:700;font-size:40px;line-height:42px;color:var(--blue);letter-spacing:2px}
.brand-tag{font-family:"Roboto",sans-serif;font-weight:700;font-size:11px;color:#6f8190;letter-spacing:.2px}
.contact-top{position:absolute;right:93px;top:20px;display:flex;gap:8px;align-items:center}
.contact-top .sq{width:28px;height:28px;background:var(--green);display:flex;align-items:center;justify-content:center}
.contact-top .tel{font-family:"Roboto",sans-serif;font-weight:500;font-size:17px;line-height:17px}
.contact-top .mail{font-size:11px;color:var(--body)}
.nav{position:absolute;left:0;top:73px;width:1200px;height:41px;background:var(--grad)}
.nav ul{list-style:none;display:flex;position:absolute;left:93px;top:14px;gap:41px}
.nav li{font-family:"Roboto",sans-serif;font-size:11.5px;color:rgba(255,255,255,.85)}
.nav li.on{color:#fff;font-weight:500}
.social{position:absolute;right:93px;top:13px;display:flex;gap:18px}
.social span{width:15px;height:15px;border-radius:50%;background:#fff;opacity:.9}

/* hero */
.hero{position:absolute;left:0;top:114px;width:1200px;height:486px;background:linear-gradient(90deg,#e9ebf4 0%,#eceef5 50%,#e2e5ee 100%)}
.hero-photo{position:absolute;right:0;top:0;width:660px;height:486px;background:linear-gradient(120deg,#eef0f5 0%,#d9dde6 45%,#3c4a78 80%,#25306a 100%)}
.hero-text{position:absolute;left:92px;top:128px}
.hero-text .k1{font-family:"Roboto",sans-serif;font-size:27px;color:#2f3438}
.hero-text .k2{font-family:"Roboto",sans-serif;font-weight:700;font-size:46px;line-height:52px;color:var(--green)}
.hero-text .k3{font-family:"Roboto",sans-serif;font-weight:700;font-size:46px;line-height:52px;color:var(--ink)}
.hero-text .sub{font-size:20px;margin-top:6px}
.btn{display:inline-block;background:var(--grad);color:#fff;font-family:"Roboto",sans-serif;font-weight:700;font-size:12px;padding:14px 20px}
.hero-text .btn{margin-top:22px}
.dots{position:absolute;left:590px;top:452px;display:flex;gap:3px}
.dots i{width:5px;height:4px;background:#2c3a58}
.dots i:first-child{background:var(--blue)}

/* presentation */
.pres-img{position:absolute;left:93px;top:687px;width:465px;height:428px;border-radius:6px;background:linear-gradient(150deg,#d8dadd 0%,#c3c6cb 40%,#3f66b8 75%,#2c4da0 100%)}
.pres{position:absolute;left:600px;top:726px;width:510px}
.pres .eyebrow{font-size:19px;color:#6f767c}
.pres h2{font-family:"Roboto",sans-serif;font-weight:700;font-size:38px;line-height:42px;margin-top:4px}
.pres h2 em{font-style:normal;color:var(--teal)}
.pres p{font-size:15px;line-height:22px;color:var(--body);margin-top:22px}
.pres .btn{margin-top:26px}

/* services */
.services{position:absolute;left:0;top:1194px;width:1200px;height:436px;background:var(--grad);color:#fff;text-align:center}
.services h2{font-family:"Roboto",sans-serif;font-weight:700;font-size:38px;margin-top:46px}
.services .lead{font-size:15px;margin-top:4px}
.svc{position:absolute;top:145px;width:280px;text-align:center}
.ring{width:118px;height:118px;border-radius:50%;background:rgba(20,90,100,.3);margin:0 auto;display:flex;align-items:center;justify-content:center}
.ring b{width:92px;height:92px;border-radius:50%;background:#fff;display:flex;align-items:center;justify-content:center}
.svc h3{font-family:"Roboto",sans-serif;font-weight:400;font-size:20px;margin-top:20px}
.svc p{font-size:13px;line-height:18px;margin-top:6px}

/* contact */
.contact{position:absolute;left:93px;top:1593px;width:1013px;height:427px;background:#fff;border-radius:6px;box-shadow:0 6px 20px rgba(0,0,0,.08);overflow:hidden}
.map{position:absolute;left:0;top:0;width:490px;height:427px;background:radial-gradient(circle at 55% 45%,#2e3032 0%,#1c1d1f 60%,#0e0e0f 100%)}
.form{position:absolute;left:524px;top:42px;width:456px}
.form h2{font-family:"Roboto",sans-serif;font-weight:700;font-size:38px}
.form h2 em{font-style:normal;color:var(--teal)}
.form .lead{font-size:13px;color:var(--body);margin-top:4px}
.fields{display:grid;grid-template-columns:221px 221px;gap:8px 8px;margin-top:30px}
.field{height:31px;border:1px solid var(--line);font-size:11px;color:#7b8187;padding:9px 8px}
.field.wide{grid-column:1/3;height:114px}
.send{position:absolute;right:0;top:323px;background:var(--grad);color:#fff;font-family:"Roboto",sans-serif;font-weight:700;font-size:10px;width:82px;height:33px;display:flex;align-items:center;justify-content:center}

/* information */
.info{position:absolute;left:0;top:2095px;width:1200px;text-align:center}
.info h2{font-family:"Roboto",sans-serif;font-weight:700;font-size:38px}
.info .lead{font-size:16px;color:var(--body);margin-top:8px}
.inf{position:absolute;top:102px;width:300px;text-align:center}
.dot{width:72px;height:72px;border-radius:50%;background:var(--grad);margin:0 auto;display:flex;align-items:center;justify-content:center}
.inf h3{font-family:"Roboto",sans-serif;font-weight:400;font-size:17px;margin-top:11px}
.inf p{font-size:13px;line-height:21px;color:var(--body);margin-top:6px}

/* cta */
.cta{position:absolute;left:0;top:2430px;width:1200px;height:237px;background:var(--grad);color:#fff;text-align:center}
.cta .t1{font-family:"Roboto",sans-serif;font-weight:700;font-size:34px;margin-top:42px;line-height:36px}
.cta .t2{font-family:"Roboto",sans-serif;font-weight:700;font-size:46px;line-height:48px}
.cta p{font-size:16px;line-height:25px;margin:18px auto 0;width:840px}

/* footer */
.footer{position:absolute;left:0;top:2667px;width:1200px;height:291px;background:var(--footer);color:#fff}
.fcol{position:absolute;top:54px}
.fcol h4{font-family:"Roboto",sans-serif;font-weight:400;font-size:19px;margin-bottom:10px}
.fcol li{list-style:none;font-size:12px;color:#c9cdd0;line-height:28.5px;display:flex;align-items:center;gap:9px}
.fcol li i{width:12px;height:12px;border-radius:50%;background:#fff}
.fbrand{position:absolute;left:830px;top:60px;width:280px;text-align:center}
.fbrand .name{font-family:"Roboto",sans-serif;font-weight:700;font-size:82px;line-height:84px;color:var(--teal);letter-spacing:4px}
.fbrand .tag{font-family:"Roboto",sans-serif;font-weight:500;font-size:17px;margin-top:4px}
.copy{position:absolute;left:0;top:231px;width:1200px;text-align:center;font-size:12px;color:#6f7478}
.copy em{font-style:normal;color:var(--green)}
</style>
</head>
<body>

<header class="topbar">
  <div class="brand">
    <div class="brand-name">ORV</div>
    <div class="brand-tag">SOLARIS ATELIER CLIMATIQUE</div>
  </div>
  <div class="contact-top">
    <div class="sq"><svg width="14" height="14" viewBox="0 0 14 14"><path d="M1 7 L13 1 L10 13 L7 8 Z" fill="#fff"/></svg></div>
    <div><div class="tel">04 70 12 34 56</div><div class="mail">contact@solaris-atelier.fr</div></div>
  </div>
</header>

<nav class="nav">
  <ul>
    <li class="on">PRESENTATION</li><li>SERVICES</li><li>ACHIEVEMENTS</li><li>CONTACT</li>
  </ul>
  <div class="social"><span></span><span></span><span></span></div>
</nav>

<section class="hero">
  <div class="hero-photo" role="img" aria-label="Technician in navy uniform cleaning a wall-mounted air conditioning unit"></div>
  <div class="hero-text">
    <div class="k1">SOLARIS</div>
    <div class="k2">CLIMATE</div>
    <div class="k3">ATELIER GRENOBLE</div>
    <div class="sub">The Solution To Your Maintenance Problem</div>
    <a class="btn">GET STRATED</a>
  </div>
  <div class="dots"><i></i><i></i><i></i></div>
</section>

<div class="pres-img" role="img" aria-label="Technician servicing a ceiling cassette air conditioner while carrying a toolbox"></div>
<section class="pres">
  <div class="eyebrow">PRESENTATION</div>
  <h2><em>SOLARIS</em> CLIMATE<br>ATELIER</h2>
  <p>Sed ut perspiciatis unde omnis iste natus error sit voluptatem accusantium doloremque laudantium, totam rem aperiam, eaque ipsa quae ab illo inventore veritatis et quasi architecto beatae vitae dicta sunt explicabo. Nemo enim ipsam voluptatem quia voluptas sit aspernatur aut odit aut fugit, sed quia consequuntur magni dolores eos qui ratione voluptatem sequi nesciunt. Neque porro quisquam est, qui dolorem ipsum quia dolor sit amet, consectetur.</p>
  <a class="btn">READ MORE</a>
</section>

<section class="services">
  <h2>OUR SERVICES</h2>
  <div class="lead">Sed ut perspiciatis unde omnis iste natus error sit voluptatem accusantium</div>
  <div class="svc" style="left:122px">
    <div class="ring"><b><svg width="54" height="50" viewBox="0 0 54 50"><path d="M4 14 L18 7 L32 14 L18 21 Z" fill="#d8f1f7"/><path d="M4 14 V30 L18 37 V21 Z" fill="#a9dcea"/><path d="M32 14 V30 L18 37 V21 Z" fill="#82cde0"/><path d="M22 26 L36 19 L50 26 L36 33 Z" fill="#d8f1f7"/><path d="M22 26 V42 L36 49 V33 Z" fill="#a9dcea"/><path d="M50 26 V42 L36 49 V33 Z" fill="#82cde0"/></svg></b></div>
    <h3>AIR CONDITIONING</h3>
    <p>Sed ut perspiciatis unde omnis iste natus error<br>sit voluptatem accusantium</p>
  </div>
  <div class="svc" style="left:460px">
    <div class="ring"><b><svg width="44" height="56" viewBox="0 0 44 56"><path d="M22 2 C26 14 40 20 40 36 A18 18 0 0 1 4 36 C4 26 10 22 12 14 C16 20 18 22 20 22 C20 14 20 8 22 2 Z" fill="#f2572b"/><path d="M22 30 C26 36 30 38 30 44 A8 8 0 0 1 14 44 C14 38 20 36 22 30 Z" fill="#ffb32b"/></svg></b></div>
    <h3>HEATING</h3>
    <p>Sed ut perspiciatis unde omnis iste natus error<br>sit voluptatem accusantium</p>
  </div>
  <div class="svc" style="left:797px">
    <div class="ring"><b><svg width="56" height="56" viewBox="0 0 56 56"><g fill="#5fb6c9"><ellipse cx="28" cy="14" rx="8" ry="13"/><ellipse cx="28" cy="14" rx="8" ry="13" transform="rotate(72 28 28)"/><ellipse cx="28" cy="14" rx="8" ry="13" transform="rotate(144 28 28)"/><ellipse cx="28" cy="14" rx="8" ry="13" transform="rotate(216 28 28)"/><ellipse cx="28" cy="14" rx="8" ry="13" transform="rotate(288 28 28)"/></g><circle cx="28" cy="28" r="6" fill="#d9eef3"/></svg></b></div>
    <h3>AIR TREATMENT</h3>
    <p>Sed ut perspiciatis unde omnis iste natus error<br>sit voluptatem accusantium</p>
  </div>
</section>

<section class="contact">
  <div class="map" role="img" aria-label="Dark street map showing the company location marker"></div>
  <div class="form">
    <h2><em>GET</em> IN TOUCH</h2>
    <div class="lead">Sed ut perspiciatis unde omnis iste natus error sit voluptatem accusantium</div>
    <div class="fields">
      <div class="field">Name:</div><div class="field">Email:</div>
      <div class="field">Phone:</div><div class="field">Company:</div>
      <div class="field wide">Comments:</div>
    </div>
    <div class="send">SEND</div>
  </div>
</section>

<section class="info">
  <h2>INFORMATION</h2>
  <div class="lead">The Solution To Your Maintenance Problem</div>
  <div class="inf" style="left:112px">
    <div class="dot"><svg width="24" height="30" viewBox="0 0 24 30"><path d="M12 1 A10 10 0 0 1 22 11 C22 18 12 29 12 29 C12 29 2 18 2 11 A10 10 0 0 1 12 1 Z" fill="#fff"/><circle cx="12" cy="11" r="4" fill="#3aa0ad"/></svg></div>
    <h3>ADDRESS</h3>
    <p>14 Rue des Tilleuls,<br>38100 SAINT AUBIN DU PONT</p>
  </div>
  <div class="inf" style="left:450px">
    <div class="dot"><svg width="26" height="32" viewBox="0 0 26 32"><path d="M7 2 L12 2 L13 9 L9 11 C10 17 13 21 17 24 L20 20 L25 22 L24 29 C14 30 4 20 3 8 Z" fill="#fff"/></svg></div>
    <h3>PHONE</h3>
    <p>04 70 12 34 56 &nbsp;|&nbsp; 04 70 65 43 21</p>
  </div>
  <div class="inf" style="left:788px">
    <div class="dot"><svg width="36" height="26" viewBox="0 0 36 26"><rect x="1" y="1" width="34" height="24" fill="none" stroke="#fff" stroke-width="2"/><path d="M1 1 L18 15 L35 1 M1 25 L14 12 M35 25 L22 12" fill="none" stroke="#fff" stroke-width="2"/></svg></div>
    <h3>ADDRESS</h3>
    <p>contact@solaris-atelier.fr</p>
  </div>
</section>

<section class="cta">
  <div class="t1">EXCEPTEUR</div>
  <div class="t2">SINT OCCAECAT CUPIDATAT</div>
  <p>Lorem ipsum dolor sit amet, consectetur adipisicing elit, sed do eiusmod tempor incididunt ut labore and dolore magna aliqua. Ut enim ad minim veniam, quis nostrud exercitation ullamco laboris nisi ut.</p>
</section>

<footer class="footer">
  <div class="fcol" style="left:93px">
    <h4>QUICK LINKS</h4>
    <ul><li>Presentation</li><li>Services</li><li>Achievment</li><li>Contact Us</li></ul>
  </div>
  <div class="fcol" style="left:311px">
    <h4>SERVICES</h4>
    <ul><li>Air Conditioning</li><li>Heating</li><li>Air Treatment</li></ul>
  </div>
  <div class="fcol" style="left:515px">
    <h4>FOLLOW US</h4>
    <ul><li><i></i>Fotoboard</li><li><i></i>Chirper</li><li><i></i>Revuo</li></ul>
  </div>
  <div class="fbrand">
    <div class="name">ORV</div>
    <div class="tag">SOLARIS CLIMATE ATELIER</div>
  </div>
  <div class="copy">COPYRIGHT © 2020 <em>ORV</em>. ALL RIGHTS RESERVED.</div>
</footer>

</body>
</html>
```